Business Card Design

Rubber roller servicing company. Specializing in rubber to metal bonding. Serving various industries including, pharmaceutical, textile, plastic extrusion, polythene bag converting, laminating and the food industries.

Industry/Entity Type

Plastic

Contact Information for Business Card

Harwick Cylinder & Polymer Co Ltd, Desmond Pallister, Managing Director, Unit at Fernholm, Kestrel Lane, Oakbrewe, Thornsby, North Ashdale, HX9 2TZ, Tel 01632 960418, Fax 01632 960773, email info@harwickcylinder.co.uk,

```html
<!DOCTYPE html>
<html lang="en">
<head>
<meta charset="utf-8">
<title>Harwick Cylinder &amp; Polymer Co Ltd — Business Card</title>
<link rel="stylesheet" href="https://fonts.googleapis.com/css2?family=Lato:wght@400&display=swap">
<style>
  :root {
    --paper: #ffffff;
    --charcoal: #333133;
    --leaf: #62bb46;
    --ink: #2b2a2b;
    --light-text: #ffffff;
  }
  * { margin: 0; padding: 0; box-sizing: border-box; }
  html, body { width: 1200px; height: 791px; overflow: hidden; background: var(--paper); }
  .card {
    position: relative;
    width: 1200px;
    height: 791px;
    background: var(--paper);
    font-family: "Lato", sans-serif;
    color: var(--light-text);
  }
  .company-name {
    position: absolute;
    left: 100px;
    top: 168px;
    width: 1000px;
    height: 50px;
  }
  .company-name text {
    font-family: "Lato", sans-serif;
    font-weight: 400;
    font-size: 36px;
    fill: var(--ink);
  }
  .contact-band {
    position: absolute;
    left: 0;
    top: 305px;
    width: 1200px;
    height: 374px;
    background: var(--charcoal);
  }
  .accent-band {
    position: absolute;
    left: 0;
    top: 691px;
    width: 1200px;
    height: 100px;
    background: var(--leaf);
  }
  .contact-row {
    position: absolute;
    left: 100px;
    display: flex;
    align-items: center;
    gap: 18px;
  }
  .contact-row .icon { width: 53px; flex: none; }
  .contact-row p {
    font-size: 26.5px;
    line-height: 34.5px;
  }
  .row-phone { top: 366px; }
  .row-web { top: 453px; }
  .row-address { top: 543px; }
  .person {
    position: absolute;
    right: 100px;
    top: 442px;
    text-align: right;
  }
  .person-name {
    font-size: 46px;
    line-height: 54px;
    font-weight: 400;
  }
  .person-role {
    font-size: 29px;
    line-height: 34px;
  }
</style>
</head>
<body>
<div class="card">
  <svg class="company-name" viewBox="0 0 1000 50" aria-label="Harwick Cylinder &amp; Polymer Co Ltd">
    <text x="0" y="38" textLength="1000" lengthAdjust="spacing">HARWICK CYLINDER &amp; POLYMER CO LTD</text>
  </svg>

  <div class="contact-band"></div>
  <div class="accent-band"></div>

  <div class="contact-row row-phone">
    <svg class="icon" viewBox="0 0 53 50" aria-hidden="true" fill="#fff">
      <path d="M2 14 C2 4 51 4 51 14 L51 19 L40 19 L40 13 C33 10 20 10 13 13 L13 19 L2 19 Z"/>
      <path d="M15 18 L38 18 L46 34 L46 48 L7 48 L7 34 Z"/>
      <g fill="#333133">
        <rect x="19" y="26" width="4" height="3"/><rect x="25" y="26" width="4" height="3"/><rect x="31" y="26" width="4" height="3"/>
        <rect x="19" y="31" width="4" height="3"/><rect x="25" y="31" width="4" height="3"/><rect x="31" y="31" width="4" height="3"/>
        <rect x="19" y="36" width="4" height="3"/><rect x="25" y="36" width="4" height="3"/><rect x="31" y="36" width="4" height="3"/>
      </g>
    </svg>
    <p>+ 163-296-0418<br>+ 16-329-60773</p>
  </div>

  <div class="contact-row row-web">
    <svg class="icon" viewBox="0 0 53 56" aria-hidden="true" fill="none" stroke="#fff" stroke-width="3.5">
      <circle cx="26.5" cy="28" r="24"/>
      <ellipse cx="26.5" cy="28" rx="10" ry="24"/>
      <line x1="26.5" y1="4" x2="26.5" y2="52"/>
      <line x1="2.5" y1="28" x2="50.5" y2="28"/>
      <path d="M6 16 H47 M6 40 H47"/>
    </svg>
    <p>info@harwickcylinder.co.uk<br>www.harwickcylinder.co.uk</p>
  </div>

  <div class="contact-row row-address">
    <svg class="icon" viewBox="0 0 53 54" aria-hidden="true" fill="#fff">
      <path d="M26.5 2 L53 26 L48 31 L26.5 11 L5 31 L0 26 Z"/>
      <path d="M8 30 L26.5 14 L45 30 L45 54 L32 54 L32 38 L21 38 L21 54 L8 54 Z"/>
    </svg>
    <p>Unit at Fernholm, Kestrel Lane,<br>Oakbrewe, Thornsby,<br>North Ashdale, HX9 2TZ</p>
  </div>

  <div class="person">
    <h1 class="person-name">DESMOND PALLISTER</h1>
    <p class="person-role">Managing Director</p>
  </div>
</div>
</body>
</html>
```